Architectural Design Build company needs a direct mail flyer

We are a fully service Design Build company who specialize in luxury custom and pre-designed new homes and major home renovations. Our team consists of seasoned architectural, interior design and general contracting professionals all under one roof. We offer clients a transparent, streamlined process to maximize their investment and completion on a timely basis. Leveraging photography and a few before and after and also our Best Builder Awards.

Target Market(s)

Homeowners and buyers between 40-60 years old and financial investment of $300k or more for renovations and $1,000,000 or more for new construction.

Industry/Entity Type

homebuilding and renovations

Colors

Designer to choose colors to be used in the design.

Requirements
Must have
• The construction segments we are focusing this mailer on are transformative renovations and professionally designed custom new homes. . Should have the Pelbrook Before kitchen and after as well as the exterior before and after. and new construction elevation photos.
Nice to have
• WOuld like to see two befores and afters highlighted, mention that are architect and designer are part of the team from start to finish,

```html
<!DOCTYPE html>
<html lang="en">
<head>
<meta charset="utf-8">
<title>KORVAN Design Build Flyer</title>
<link rel="stylesheet" href="https://fonts.googleapis.com/css2?family=Poppins:wght@400;500;600;700;800&display=swap">
<style>
  :root {
    --ink: #1f1c1a;
    --band: #2b2724;
    --lime: #d8e35a;
    --panel: #f5f2ef;
    --rule: #cfcac4;
    --white: #ffffff;
    --wood: #5a2f1f;
    --sky: #eef0ec;
    --lawn: #4f8a3a;
  }
  * { margin: 0; padding: 0; box-sizing: border-box; }
  html, body { width: 1200px; height: 655px; overflow: hidden; background: var(--white); }
  body { font-family: "Poppins", sans-serif; color: var(--ink); position: relative; }

  .topbar { position: absolute; left: 0; top: 0; width: 1200px; height: 54px; border-bottom: 1px solid var(--rule); }
  .topbar .corner { position: absolute; top: 0; }
  .topbar .divider { position: absolute; top: 0; width: 1px; height: 54px; background: var(--rule); }
  .brand { position: absolute; left: 121px; top: 8px; font-weight: 800; font-size: 34px; letter-spacing: 3px; line-height: 38px; color: var(--ink); }

  .hero-photo {
    position: absolute; left: 0; top: 190px; width: 811px; height: 397px;
    background:
      linear-gradient(to bottom, rgba(255,255,255,1) 0%, rgba(255,255,255,0) 30%),
      linear-gradient(to bottom, #dfe3da 0%, #b79a6a 35%, #e9e7e2 50%, #f1efeb 68%, #8f8a84 84%, var(--lawn) 100%);
  }

  .headline { position: absolute; left: 50px; top: 100px; font-weight: 800; font-size: 32.5px; line-height: 37px; letter-spacing: -0.3px; text-transform: uppercase; }
  .tagline { position: absolute; left: 50px; top: 177px; font-weight: 400; font-size: 17px; line-height: 24px; }

  .footer-band { position: absolute; left: 0; top: 587px; width: 811px; height: 68px; background: var(--band); }
  .footer-band .rule { position: absolute; left: 0; width: 811px; height: 1px; background: #4a4440; }
  .footer-logo { position: absolute; left: 13px; top: 16px; width: 96px; height: 36px; background: var(--lime); color: var(--ink); font-weight: 800; font-size: 20px; letter-spacing: 2px; line-height: 36px; text-align: center; }
  .footer-cta { position: absolute; left: 140px; top: 24px; display: flex; align-items: center; gap: 8px; color: var(--white); font-weight: 600; font-size: 12.5px; line-height: 20px; white-space: nowrap; }
  .footer-cta .contact { display: flex; align-items: center; gap: 3px; font-size: 13px; }

  .showcase { position: absolute; left: 803px; top: 55px; width: 397px; height: 600px; background: var(--panel); }
  .project-title { position: absolute; font-weight: 700; font-size: 22px; line-height: 26px; text-transform: uppercase; }
  .project-note { position: absolute; font-weight: 400; font-size: 9px; line-height: 12px; }
  .compare { position: absolute; display: flex; gap: 2px; }
  .compare .shot { position: relative; height: 100%; }
  .compare .label { position: absolute; bottom: 8px; left: 0; right: 0; text-align: center; color: var(--white); font-weight: 700; font-size: 14px; letter-spacing: 0.3px; }
  .handle { position: absolute; width: 24px; height: 24px; border-radius: 50%; background: var(--white); box-shadow: 0 1px 3px rgba(0,0,0,.25); }
</style>
</head>
<body>
  <header class="topbar">
    <svg class="corner" style="left:0" width="89" height="54" viewBox="0 0 89 54">
      <line x1="0" y1="40" x2="42" y2="0" stroke="#dfe59a" stroke-width="1"/>
      <line x1="46" y1="54" x2="89" y2="12" stroke="#dfe59a" stroke-width="1"/>
    </svg>
    <div class="divider" style="left:89px"></div>
    <div class="brand">KORVAN</div>
    <div class="divider" style="left:1114px"></div>
    <svg class="corner" style="left:1115px" width="85" height="54" viewBox="0 0 85 54">
      <line x1="0" y1="44" x2="44" y2="0" stroke="#dfe59a" stroke-width="1"/>
      <line x1="48" y1="54" x2="85" y2="18" stroke="#dfe59a" stroke-width="1"/>
    </svg>
  </header>

  <div class="hero-photo" role="img" aria-label="Newly built white two-storey craftsman home with wraparound porch, lawn and mature trees"></div>

  <h1 class="headline">Transform your home. Design &amp;<br>build with award-winning experts.</h1>
  <p class="tagline">Luxury Renovations &amp; Custom Homes by One Team</p>

  <footer class="footer-band">
    <div class="rule" style="top:15px"></div>
    <div class="rule" style="top:52px"></div>
    <div class="footer-logo">KORVAN</div>
    <div class="footer-cta">
      <span>Call Now to Schedule a free consultation</span>
      <span class="contact">
        <svg width="12" height="9" viewBox="0 0 12 9"><rect x="0" y="0" width="12" height="9" rx="1" fill="#d8e35a"/><path d="M0.5 0.8 L6 5 L11.5 0.8" fill="none" stroke="#2b2724" stroke-width="1.2"/></svg>
        korvanbuild.com
      </span>
      <span class="contact">
        <svg width="11" height="11" viewBox="0 0 24 24"><path d="M6.6 10.8a15.1 15.1 0 0 0 6.6 6.6l2.2-2.2a1 1 0 0 1 1-.25 11.4 11.4 0 0 0 3.6.57 1 1 0 0 1 1 1V20a1 1 0 0 1-1 1A17 17 0 0 1 3 4a1 1 0 0 1 1-1h3.5a1 1 0 0 1 1 1c0 1.25.2 2.45.57 3.57a1 1 0 0 1-.25 1z" fill="#d8e35a"/></svg>
        (555) 014-2290
      </span>
    </div>
  </footer>

  <section class="showcase">
    <h2 class="project-title" style="left:49px;top:52px">Pelbrook Kitchen</h2>
    <p class="project-note" style="left:50px;top:79px">A complete kitchen transformation – designed and built by KORVAN</p>
    <div class="compare" style="left:45px;top:105px;width:315px;height:180px">
      <div class="shot" role="img" aria-label="Kitchen before: dark cherry wood cabinets and dated counters"
           style="width:156px;clip-path:polygon(0 0,100% 0,100% 100%,22px 100%,0 74%);background:linear-gradient(to bottom,#4a2a1c 0%,#6e3b26 35%,#8b7a66 55%,#5a2f1f 75%,#2e2623 100%)">
        <span class="label">BEFORE</span>
      </div>
      <div class="shot" role="img" aria-label="Kitchen after: white cabinetry, stainless hood and marble island"
           style="width:157px;clip-path:polygon(0 0,86% 0,100% 14%,100% 100%,0 100%);background:linear-gradient(to bottom,#f2f0ec 0%,#e5e2dc 40%,#d6d3cd 65%,#6b6560 88%,#3a3430 100%)">
        <span class="label">AFTER</span>
      </div>
      <div class="handle" style="left:145px;top:78px"></div>
    </div>

    <h2 class="project-title" style="left:38px;top:310px">Exterior</h2>
    <p class="project-note" style="left:39px;top:339px">Exterior elevation updated for curb appeal and modern living”</p>
    <div class="compare" style="left:39px;top:367px;width:314px;height:180px">
      <div class="shot" role="img" aria-label="Before: plain kitchen with white cabinets and dark granite counters"
           style="width:155px;background:linear-gradient(to bottom,#e8e8e6 0%,#d4d4d0 40%,#3a3836 62%,#2a2826 100%)">
        <span class="label">BEFORE</span>
      </div>
      <div class="shot" role="img" aria-label="After: renovated white home exterior with porch and fresh lawn"
           style="width:157px;clip-path:polygon(0 0,92% 0,100% 10%,100% 100%,0 100%);background:linear-gradient(to bottom,#f0efec 0%,#d9d7d2 30%,#5f9a44 50%,#4f8a3a 72%,#4a3a30 74%,#3a2e28 100%)">
        <span class="label">AFTER</span>
      </div>
      <div class="handle" style="left:144px;top:78px"></div>
    </div>
  </section>

  <svg style="position:absolute;left:0;top:0;width:0;height:0" aria-hidden="true"></svg>
</body>
</html>
```